Business Card for boutique psychology business

Business card for boutique psychology practice in Melbourne. I want them to be relatively simply with the logo and backing colour taking up the front side. Then, text on the back, with my name; professional title (Clinical Psychologist); website - torvinpsychology.com.au; email: hello@torvinpsychology.com.au; insta: @torvin.psychology.emdr
Back should also have the words: Connect. Integrate. Evolve
Fonts used for logo are: Mikea Demo and Gotham Medium. Use something for back text that will compliment these.
Brand colours uploaded below. I'd like to see options in both olive and blush.

```html
<!DOCTYPE html>
<html lang="en">
<head>
<meta charset="UTF-8">
<title>Torvin Psychology – Business Cards</title>
<link rel="stylesheet" href="https://fonts.googleapis.com/css2?family=Montserrat:wght@400;500;600&display=swap">
<style>
  :root {
    --backdrop: #ecedee;
    --olive: #4a5431;
    --blush: #ecccbf;
    --cream: #f6f3ee;
    --ink: #4a5230;
    --logo-light: #ecd3c6;
  }
  * { margin: 0; padding: 0; box-sizing: border-box; }
  html, body {
    width: 1200px;
    height: 800px;
    overflow: hidden;
    background: var(--backdrop);
    font-family: "Montserrat", sans-serif;
  }
  .sheet {
    position: relative;
    width: 1200px;
    height: 800px;
  }
  .card {
    position: absolute;
    width: 458px;
  }
  .card--front { top: 78px; height: 260px; display: flex; align-items: center; justify-content: center; }
  .card--back { top: 421px; height: 283px; background: var(--cream); color: var(--ink); }
  .col-olive { left: 63px; }
  .col-blush { left: 664px; }
  .card--olive { background: var(--olive); }
  .card--blush { background: var(--blush); }

  .wordmark {
    text-align: center;
    font-weight: 500;
    margin-top: -8px;
  }
  .card--olive .wordmark { color: var(--logo-light); }
  .card--blush .wordmark { color: var(--ink); }
  .wordmark__name {
    display: block;
    font-size: 56px;
    line-height: 1;
    letter-spacing: -1px;
  }
  .wordmark__sub {
    display: block;
    font-size: 16px;
    margin-top: 8px;
    letter-spacing: 0.2px;
  }

  .back__name {
    position: absolute;
    left: 38px;
    top: 34px;
    font-size: 20px;
    font-weight: 600;
  }
  .back__title {
    position: absolute;
    left: 38px;
    top: 64px;
    font-size: 13.5px;
    font-weight: 600;
  }
  .contact {
    position: absolute;
    left: 38px;
    top: 105px;
    list-style: none;
    font-size: 15.5px;
    font-weight: 400;
  }
  .contact li {
    height: 29px;
    display: flex;
    align-items: center;
  }
  .contact__dot {
    width: 13px;
    height: 13px;
    margin-right: 5px;
  }
  .back__tagline {
    position: absolute;
    left: 37px;
    top: 222px;
    font-size: 20px;
    font-weight: 400;
    letter-spacing: 0.2px;
  }
</style>
</head>
<body>
<main class="sheet">

  <section class="card card--front card--olive col-olive" aria-label="Front, olive">
    <div class="wordmark">
      <span class="wordmark__name">torvin</span>
      <span class="wordmark__sub">psychology + EMDR</span>
    </div>
  </section>

  <section class="card card--front card--blush col-blush" aria-label="Front, blush">
    <div class="wordmark">
      <span class="wordmark__name">torvin</span>
      <span class="wordmark__sub">psychology + EMDR</span>
    </div>
  </section>

  <section class="card card--back col-olive" aria-label="Back, olive option">
    <h1 class="back__name">Marisol Hendry</h1>
    <p class="back__title">Clinical Psychologist</p>
    <ul class="contact">
      <li>torvinpsychology.com.au</li>
      <li>hello@torvinpsychology.com.au</li>
      <li><svg class="contact__dot" viewBox="0 0 13 13" aria-hidden="true"><circle cx="6.5" cy="6.5" r="5.5" fill="none" stroke="currentColor" stroke-width="1.6"/></svg>@torvin.psychology.emdr</li>
    </ul>
    <p class="back__tagline">Connect. Integrate. Evolve.</p>
  </section>

  <section class="card card--back col-blush" aria-label="Back, blush option">
    <h1 class="back__name">Marisol Hendry</h1>
    <p class="back__title">Clinical Psychologist</p>
    <ul class="contact">
      <li>torvinpsychology.com.au</li>
      <li>hello@torvinpsychology.com.au</li>
      <li><svg class="contact__dot" viewBox="0 0 13 13" aria-hidden="true"><circle cx="6.5" cy="6.5" r="5.5" fill="none" stroke="currentColor" stroke-width="1.6"/></svg>@torvin.psychology.emdr</li>
    </ul>
    <p class="back__tagline">Connect. Integrate. Evolve.</p>
  </section>

</main>
</body>
</html>
```